Social News web page design website name Vorlet.

I need a web design for a start up project called Vorlet based in Sydney. Its a social news website. it helps people to get centralized news and people can have their own profiles where they can post there thoughts and comments and it will be free to signup and usage as well.

I would like to see designs that use the latest pelican scaffold framework and are mobile compatible. only need 2 pages a home page kind of similar to
plonk (http://plonk.example/) and a profile that's a next gen user profile page I will leave that to you imaginations

this is my previous design I did on my own http://www.vorlet.example/

Target Market(s)

target market is 13 and up and anyone who likes or uses social media and would be able to understand the site

Industry/Entity Type

News

Requirements
Must have
• 1.) using pelican scaffold. 2) a home page similar to plonk (http://plonk.example/) or even better free to use your imagination 3) a next gen profile page better the one i made on my own which is this one (http://www.vorlet.example/profile/hollisbrackett) 4) for mobile navigation, have a mobile navigation something similar to http://slidepanel.quenrow.example/
Nice to have
• 1) a sexy navigation and layout for both desktop and mobile phones. i will leave that to you imaginations. 2) social medial buttons like to sign-in with and also to post a story to Chatterly or pelican 3) a user settings page (but not necessary) 4) a login or signup (but not necessary)

```html
<!DOCTYPE html>
<html lang="en">
<head>
<meta charset="utf-8">
<title>Vorlet — Social News</title>
<link rel="stylesheet" href="https://fonts.googleapis.com/css2?family=Questrial&family=Arimo:wght@400;700&display=swap">
<style>
:root{
  --page:#f7f7f7;
  --white:#ffffff;
  --ink:#555a5e;
  --ink-soft:#8a8f93;
  --ink-faint:#a9adb0;
  --line:#e3e3e3;
  --blue:#3a86c8;
  --blue-deep:#2f7bd0;
  --teal:#2aa6a0;
  --red:#d9453b;
  --faq-band:#e9ecee;
  --footer:#3a3a3a;
  --footer-low:#eeeeee;
}
*{box-sizing:border-box;margin:0;padding:0}
html,body{width:1200px;height:2605px;overflow:hidden}
body{background:var(--page);font-family:"Arimo",Arial,sans-serif;color:var(--ink);position:relative}
a{color:inherit;text-decoration:none}
svg.icon{width:14px;height:14px;fill:currentColor;vertical-align:middle}

/* header */
.site-header{position:absolute;left:0;top:0;width:1200px;height:95px;background:linear-gradient(#fff,#f9f9f9);border-bottom:1px solid #dcdcdc;box-shadow:0 1px 3px rgba(0,0,0,.05)}
.brand{position:absolute;left:83px;top:26px;font-family:"Questrial",sans-serif;font-size:38px;line-height:40px;color:#1e1e1e;letter-spacing:-.5px}
.brand-divider{position:absolute;left:229px;top:0;width:1px;height:95px;background:#e2e2e2}
.main-nav{position:absolute;left:255px;top:38px;display:flex;gap:30px;font-family:"Questrial",sans-serif;font-size:14px;color:#555}
.main-nav .active{color:var(--blue)}
.active-bar{position:absolute;left:234px;top:89px;width:82px;height:4px;background:var(--blue);border-radius:2px}
.account-links{position:absolute;left:729px;top:38px;display:flex;gap:26px;font-family:"Questrial",sans-serif;font-size:13px}
.account-links .sign-in{color:var(--teal)}
.account-links .sign-up{color:var(--blue)}
.search{position:absolute;left:900px;top:29px;width:216px;height:36px;border:1px solid #d6d6d6;border-radius:18px;background:#fbfbfb;box-shadow:inset 0 1px 2px rgba(0,0,0,.06)}
.search span{position:absolute;left:20px;top:10px;font-style:italic;font-size:12px;color:#b0b0b0}
.search .go{position:absolute;right:-1px;top:-1px;width:44px;height:36px;border-radius:0 18px 18px 0;background:linear-gradient(#f1f3f5,#dfe4e8);border:1px solid #ccd2d7;color:var(--blue);display:flex;align-items:center;justify-content:center}

/* story grid */
.story-grid{position:absolute;left:83px;top:132px;width:1032px;display:grid;grid-template-columns:repeat(3,320px);column-gap:36px;row-gap:0}
.story-card{height:388px}
.story-photo{width:320px;height:177px;border:1px solid #d9d9d9}
.story-title{margin-top:17px;font-family:"Questrial",sans-serif;font-size:14.5px;line-height:21px;text-transform:uppercase;color:#4d5256}
.story-date{font-size:11px;color:var(--blue);margin-left:8px;white-space:nowrap}
.story-date svg{fill:var(--red);width:13px;height:13px;margin-right:6px;vertical-align:-2px}
.story-rule{margin-top:7px;height:1px;background:var(--line)}
.story-text{margin-top:12px;font-size:12px;line-height:17px;color:var(--ink-faint)}
.story-text a{color:var(--blue)}
.story-actions{margin-top:18px;display:flex;gap:22px;font-size:12px;color:var(--ink-soft)}
.story-actions span{display:flex;align-items:center;gap:6px}
.story-actions svg{width:13px;height:13px;fill:#8f9396}
.story-card.is-active .story-title{color:var(--blue)}
.story-card.is-active .story-actions,.story-card.is-active .story-actions svg{color:var(--blue);fill:var(--blue)}

/* faq */
.faq-band{position:absolute;left:0;top:1693px;width:1200px;height:200px;background:var(--faq-band);border-top:1px solid #dde1e4;border-bottom:1px solid #dde1e4}
.faq-title{position:absolute;left:83px;top:82px;font-family:"Questrial",sans-serif;font-size:38px;color:var(--blue);letter-spacing:1px}
.faq-divider{position:absolute;left:217px;top:40px;width:1px;height:120px;background:#cfd4d8}
.round-arrow{position:absolute;width:34px;height:34px;border:2px solid #b5babe;border-radius:50%;display:flex;align-items:center;justify-content:center;color:#9aa0a4}
.round-arrow.prev{left:243px;top:83px}
.round-arrow.next{left:1081px;top:83px}
.faq-item{position:absolute;left:321px;top:38px;width:712px}
.faq-q{font-family:"Questrial",sans-serif;font-size:16px;color:var(--blue)}
.faq-q svg{width:18px;height:18px;fill:none;stroke:var(--blue);stroke-width:2;margin-right:6px;vertical-align:-3px}
.faq-a{margin-top:8px;display:flex;gap:10px;font-size:12.5px;line-height:17px;color:#9aa0a4}
.faq-a b{color:var(--blue);font-size:13px}

/* stories lists */
.story-list{position:absolute;top:1960px;width:490px}
.story-list.popular{left:83px}
.story-list.recent{left:627px}
.list-head{display:flex;align-items:center;height:28px}
.list-head h2{font-family:"Questrial",sans-serif;font-weight:400;font-size:22px;color:var(--blue);white-space:nowrap}
.list-head .rail{flex:1;height:8px;margin:0 10px;background:repeating-linear-gradient(90deg,#e6e6e6 0 2px,transparent 2px 4px)}
.list-head .nav{display:flex;gap:3px}
.list-head .nav i{width:22px;height:22px;display:flex;align-items:center;justify-content:center;color:#fff}
.list-head .nav .off{background:#d3d6d9}
.list-head .nav .on{background:var(--blue-deep)}
.list-item{display:flex;gap:8px;height:92px;padding-top:18px;border-bottom:1px solid var(--line)}
.list-item:last-child{border-bottom:0}
.list-thumb{width:76px;height:64px;flex:none}
.list-text{font-size:13px;line-height:17px;color:#555a5e}
.list-actions{margin-top:6px;display:flex;gap:14px;font-size:10px;color:var(--ink-soft)}
.list-actions span{display:flex;align-items:center;gap:4px}
.list-actions svg{width:10px;height:10px;fill:#8f9396}

/* footer */
.site-footer{position:absolute;left:0;top:2414px;width:1200px;height:136px;background:var(--footer);color:#eee}
.site-footer h3{position:absolute;left:83px;top:30px;font-family:"Questrial",sans-serif;font-weight:400;font-size:21px}
.footer-links{position:absolute;left:83px;top:84px;display:flex;gap:12px;font-size:11px;color:#aaa}
.footer-links .current{color:#fff}
.footer-links em{font-style:normal;color:#777}
.footer-brand{position:absolute;left:545px;top:48px;font-family:"Questrial",sans-serif;font-size:34px;color:#e5e5e5}
.follow{position:absolute;left:910px;top:30px;font-family:"Questrial",sans-serif;font-size:21px}
.social-dots{position:absolute;left:910px;top:78px;display:flex;gap:11px}
.social-dots i{width:14px;height:14px;border-radius:50%;background:#cfcfcf}
.copyright{position:absolute;left:0;top:2550px;width:1200px;height:55px;background:var(--footer-low);text-align:center;font-size:12px;line-height:55px;color:#555}
.copyright a{color:var(--blue)}
</style>
</head>
<body>
<svg width="0" height="0" style="position:absolute">
  <defs>
    <symbol id="i-share" viewBox="0 0 16 16"><circle cx="12" cy="3" r="2.5"/><circle cx="4" cy="8" r="2.5"/><circle cx="12" cy="13" r="2.5"/><path d="M4 8L12 3M4 8l8 5" stroke="currentColor" stroke-width="1.5" fill="none"/></symbol>
    <symbol id="i-save" viewBox="0 0 16 16"><path d="M3 1h10v14l-5-4-5 4z"/></symbol>
    <symbol id="i-heart" viewBox="0 0 16 16"><path d="M8 15L2 9C-1 6 2 0 8 4c6-4 9 2 6 5z"/></symbol>
    <symbol id="i-cal" viewBox="0 0 16 16"><path d="M1 3h14v12H1zM3 0h2v3H3zm8 0h2v3h-2z"/><rect x="3" y="6" width="10" height="7" fill="#fff"/></symbol>
    <symbol id="i-caret" viewBox="0 0 16 16"><path d="M3 5l5 5 5-5" stroke="currentColor" stroke-width="2" fill="none"/></symbol>
  </defs>
</svg>

<header class="site-header">
  <a class="brand" href="#">Vorlet</a>
  <div class="brand-divider"></div>
  <nav class="main-nav"><a class="active" href="#">HOME</a><a href="#">ABOUT US</a><a href="#">CONTACT US</a></nav>
  <div class="active-bar"></div>
  <div class="account-links">
    <a class="sign-in" href="#"><svg class="icon" viewBox="0 0 16 16" style="width:11px"><path d="M4 7V5a4 4 0 018 0h-2a2 2 0 00-4 0v2h7v8H2V7z"/></svg> SIGN IN</a>
    <a class="sign-up" href="#"><svg class="icon" viewBox="0 0 16 16" style="width:11px"><circle cx="8" cy="4" r="4"/><path d="M0 16c0-5 4-7 8-7s8 2 8 7z"/></svg> SIGN UP</a>
  </div>
  <div class="search"><span>Search</span><div class="go"><svg class="icon" viewBox="0 0 16 16"><circle cx="6.5" cy="6.5" r="5" fill="none" stroke="currentColor" stroke-width="2"/><path d="M10 10l5 5" stroke="currentColor" stroke-width="2.5"/></svg></div></div>
</header>

<main class="story-grid">
  <article class="story-card"><div class="story-photo" role="img" aria-label="Portrait of a smiling singer with long golden hair" style="background:linear-gradient(135deg,#8c6a3c,#d9b27a 55%,#a88052)"></div>
    <h3 class="story-title">Lorem ipsum dolor sit amet, consectetur adipisicing elit.<span class="story-date"><svg><use href="#i-cal"/></svg>7TH DEC 2014</span></h3><div class="story-rule"></div>
    <p class="story-text">Lorem Ipsum is simply dummy text of typesetting industry. Lorem Ipsum has been the industry's standard dummy text ever since the 1500s.<a href="#">LEARN MORE</a></p>
    <div class="story-actions"><span><svg><use href="#i-share"/></svg>Share Story <svg style="width:9px"><use href="#i-caret"/></svg></span><span><svg><use href="#i-save"/></svg>Save</span><span><svg><use href="#i-heart"/></svg>Vote</span></div></article>

  <article class="story-card"><div class="story-photo" role="img" aria-label="Businessman jumping on a rooftop above a city skyline" style="background:linear-gradient(#c9c9c4,#9a9a94 60%,#5e5e5a)"></div>
    <h3 class="story-title">Lorem ipsum dolor sit amet, consectetur adipisicing elit.<span class="story-date"><svg><use href="#i-cal"/></svg>7TH DEC 2014</span></h3><div class="story-rule"></div>
    <p class="story-text">Lorem Ipsum is simply dummy text of typesetting industry. Lorem Ipsum has been the industry's standard dummy text ever since the 1500s.<a href="#">LEARN MORE</a></p>
    <div class="story-actions"><span><svg><use href="#i-share"/></svg>Share Story <svg style="width:9px"><use href="#i-caret"/></svg></span><span><svg><use href="#i-save"/></svg>Save</span><span><svg><use href="#i-heart"/></svg>Vote</span></div></article>

  <article class="story-card"><div class="story-photo" role="img" aria-label="DJ with headphones raising his arms" style="background:linear-gradient(135deg,#9a9a98,#6e6c6a 60%,#3a3836)"></div>
    <h3 class="story-title">Lorem ipsum dolor sit amet, consectetur adipisicing elit.<span class="story-date"><svg><use href="#i-cal"/></svg>7TH DEC 2014</span></h3><div class="story-rule"></div>
    <p class="story-text">Lorem Ipsum is simply dummy text of typesetting industry. Lorem Ipsum has been the industry's standard dummy text ever since the 1500s.<a href="#">LEARN MORE</a></p>
    <div class="story-actions"><span><svg><use href="#i-share"/></svg>Share Story <svg style="width:9px"><use href="#i-caret"/></svg></span><span><svg><use href="#i-save"/></svg>Save</span><span><svg><use href="#i-heart"/></svg>Vote</span></div></article>

  <article class="story-card"><div class="story-photo" role="img" aria-label="Woman in a red blouse at a busy event" style="background:linear-gradient(90deg,#c23a2e,#d98a7a 45%,#b9c6d4)"></div>
    <h3 class="story-title">Lorem ipsum dolor sit amet, consectetur adipisicing elit.<span class="story-date"><svg><use href="#i-cal"/></svg>7TH DEC 2014</span></h3><div class="story-rule"></div>
    <p class="story-text">Lorem Ipsum is simply dummy text of typesetting industry. Lorem Ipsum has been the industry's standard dummy text ever since the 1500s.<a href="#">LEARN MORE</a></p>
    <div class="story-actions"><span><svg><use href="#i-share"/></svg>Share Story <svg style="width:9px"><use href="#i-caret"/></svg></span><span><svg><use href="#i-save"/></svg>Save</span><span><svg><use href="#i-heart"/></svg>Vote</span></div></article>

  <article class="story-card"><div class="story-photo" role="img" aria-label="Students reading together on a sunny lawn" style="background:linear-gradient(#6f8a3a,#9bb05a 50%,#5a6b2e)"></div>
    <h3 class="story-title">Lorem ipsum dolor sit amet, consectetur adipisicing elit.<span class="story-date"><svg><use href="#i-cal"/></svg>7TH DEC 2014</span></h3><div class="story-rule"></div>
    <p class="story-text">Lorem Ipsum is simply dummy text of typesetting industry. Lorem Ipsum has been the industry's standard dummy text ever since the 1500s.<a href="#">LEARN MORE</a></p>
    <div class="story-actions"><span><svg><use href="#i-share"/></svg>Share Story <svg style="width:9px"><use href="#i-caret"/></svg></span><span><svg><use href="#i-save"/></svg>Save</span><span><svg><use href="#i-heart"/></svg>Vote</span></div></article>

  <article class="story-card"><div class="story-photo" role="img" aria-label="Speaker in a dark jacket in front of a red banner" style="background:linear-gradient(90deg,#cfd6d8,#4a4d52 45%,#d8485e)"></div>
    <h3 class="story-title">Lorem ipsum dolor sit amet, consectetur adipisicing elit.<span class="story-date"><svg><use href="#i-cal"/></svg>7TH DEC 2014</span></h3><div class="story-rule"></div>
    <p class="story-text">Lorem Ipsum is simply dummy text of typesetting industry. Lorem Ipsum has been the industry's standard dummy text ever since the 1500s.<a href="#">LEARN MORE</a></p>
    <div class="story-actions"><span><svg><use href="#i-share"/></svg>Share Story <svg style="width:9px"><use href="#i-caret"/></svg></span><span><svg><use href="#i-save"/></svg>Save</span><span><svg><use href="#i-heart"/></svg>Vote</span></div></article>

  <article class="story-card"><div class="story-photo" role="img" aria-label="Presenters on a stage in front of a historic building" style="background:linear-gradient(#aac4dc,#8d7c66 50%,#3c4a6a)"></div>
    <h3 class="story-title">Lorem ipsum dolor sit amet, consectetur adipisicing elit.<span class="story-date"><svg><use href="#i-cal"/></svg>7TH DEC 2014</span></h3><div class="story-rule"></div>
    <p class="story-text">Lorem Ipsum is simply dummy text of typesetting industry. Lorem Ipsum has been the industry's standard dummy text ever since the 1500s.<a href="#">LEARN MORE</a></p>
    <div class="story-actions"><span><svg><use href="#i-share"/></svg>Share Story <svg style="width:9px"><use href="#i-caret"/></svg></span><span><svg><use href="#i-save"/></svg>Save</span><span><svg><use href="#i-heart"/></svg>Vote</span></div></article>

  <article class="story-card is-active"><div class="story-photo" role="img" aria-label="Man holding up a small object toward the camera" style="background:linear-gradient(90deg,#b8243a,#d7a48e 45%,#e9e2dc)"></div>
    <h3 class="story-title">Lorem ipsum dolor sit amet, consectetur adipisicing elit.<span class="story-date"><svg><use href="#i-cal"/></svg>7TH DEC 2014</span></h3><div class="story-rule"></div>
    <p class="story-text">Lorem Ipsum is simply dummy text of typesetting industry. Lorem Ipsum has been the industry's standard dummy text ever since the 1500s.<a href="#">LEARN MORE</a></p>
    <div class="story-actions"><span><svg><use href="#i-share"/></svg>Share Story <svg style="width:9px"><use href="#i-caret"/></svg></span><span><svg><use href="#i-save"/></svg>Save</span><span><svg><use href="#i-heart"/></svg>Vote</span></div></article>

  <article class="story-card"><div class="story-photo" role="img" aria-label="Close-up portrait of an actor" style="background:linear-gradient(135deg,#7a8a98,#c49a80 55%,#6a5a50)"></div>
    <h3 class="story-title">Lorem ipsum dolor sit amet, consectetur adipisicing elit.<span class="story-date"><svg><use href="#i-cal"/></svg>7TH DEC 2014</span></h3><div class="story-rule"></div>
    <p class="story-text">Lorem Ipsum is simply dummy text of typesetting industry. Lorem Ipsum has been the industry's standard dummy text ever since the 1500s.<a href="#">LEARN MORE</a></p>
    <div class="story-actions"><span><svg><use href="#i-share"/></svg>Share Story <svg style="width:9px"><use href="#i-caret"/></svg></span><span><svg><use href="#i-save"/></svg>Save</span><span><svg><use href="#i-heart"/></svg>Vote</span></div></article>

  <article class="story-card"><div class="story-photo" role="img" aria-label="Dark science fiction cityscape with a flying ship" style="background:linear-gradient(#4a4a48,#2c2c2a 60%,#5a3a2a)"></div>
    <h3 class="story-title">Lorem ipsum dolor sit amet, consectetur adipisicing elit.<span class="story-date"><svg><use href="#i-cal"/></svg>7TH DEC 2014</span></h3><div class="story-rule"></div>
    <p class="story-text">Lorem Ipsum is simply dummy text of typesetting industry. Lorem Ipsum has been the industry's standard dummy text ever since the 1500s.<a href="#">LEARN MORE</a></p>
    <div class="story-actions"><span><svg><use href="#i-share"/></svg>Share Story <svg style="width:9px"><use href="#i-caret"/></svg></span><span><svg><use href="#i-save"/></svg>Save</span><span><svg><use href="#i-heart"/></svg>Vote</span></div></article>

  <article class="story-card"><div class="story-photo" role="img" aria-label="Graduates in caps and gowns with a guide dog" style="background:linear-gradient(#7aa0c8,#3a3a5a 50%,#c06a2a)"></div>
    <h3 class="story-title">Lorem ipsum dolor sit amet, consectetur adipisicing elit.<span class="story-date"><svg><use href="#i-cal"/></svg>7TH DEC 2014</span></h3><div class="story-rule"></div>
    <p class="story-text">Lorem Ipsum is simply dummy text of typesetting industry. Lorem Ipsum has been the industry's standard dummy text ever since the 1500s.<a href="#">LEARN MORE</a></p>
    <div class="story-actions"><span><svg><use href="#i-share"/></svg>Share Story <svg style="width:9px"><use href="#i-caret"/></svg></span><span><svg><use href="#i-save"/></svg>Save</span><span><svg><use href="#i-heart"/></svg>Vote</span></div></article>

  <article class="story-card"><div class="story-photo" role="img" aria-label="Football player in a red and white kit kneeling on the field" style="background:linear-gradient(135deg,#2a4a6a,#b23030 50%,#c9a64a)"></div>
    <h3 class="story-title">Lorem ipsum dolor sit amet, consectetur adipisicing elit.<span class="story-date"><svg><use href="#i-cal"/></svg>7TH DEC 2014</span></h3><div class="story-rule"></div>
    <p class="story-text">Lorem Ipsum is simply dummy text of typesetting industry. Lorem Ipsum has been the industry's standard dummy text ever since the 1500s.<a href="#">LEARN MORE</a></p>
    <div class="story-actions"><span><svg><use href="#i-share"/></svg>Share Story <svg style="width:9px"><use href="#i-caret"/></svg></span><span><svg><use href="#i-save"/></svg>Save</span><span><svg><use href="#i-heart"/></svg>Vote</span></div></article>
</main>

<section class="faq-band">
  <h2 class="faq-title">FAQ’S</h2>
  <div class="faq-divider"></div>
  <div class="round-arrow prev"><svg class="icon" viewBox="0 0 16 16"><path d="M10 3L5 8l5 5" stroke="currentColor" stroke-width="2" fill="none"/></svg></div>
  <div class="faq-item">
    <p class="faq-q"><svg viewBox="0 0 20 20"><circle cx="10" cy="10" r="8.5"/><path d="M7.5 7.5a2.5 2.5 0 115 0c0 2-2.5 2-2.5 4M10 14v1.5"/></svg>This is Pixelform's version &nbsp;of Lorem Ipsum. Proin gravida nibh vel velit auctor aliquet.</p>
    <div class="faq-a"><b>A.</b><p>This is Pixelform's version &nbsp;of Lorem Ipsum. Proin gravida nibh vel velit auctor aliquet. Aenean sollicitudin, lorem quis bibendum auctor, nisi elit consequat ipsum, nec sagittis sem nibh id elit. Duis sed odio sit amet nibh vulputate cursus a sit amet mauris. Morbi accumsan ipsum velit. Nam nec tellus a odio tincidunt auctor a ornare odio. Sed non &nbsp;mauris vitae erat consequat auctor eu in elit. Class aptent taciti sociosqu ad litora torquent per conubia nostra, per inceptos himenaeos. Mauris in erat justo.</p></div>
  </div>
  <div class="round-arrow next"><svg class="icon" viewBox="0 0 16 16"><path d="M6 3l5 5-5 5" stroke="currentColor" stroke-width="2" fill="none"/></svg></div>
</section>

<section class="story-list popular">
  <div class="list-head"><h2>POPULAR STORIES</h2><div class="rail"></div><div class="nav"><i class="off"><svg class="icon" viewBox="0 0 16 16" style="width:10px"><path d="M10 3L5 8l5 5" stroke="#fff" stroke-width="2.5" fill="none"/></svg></i><i class="on"><svg class="icon" viewBox="0 0 16 16" style="width:10px"><path d="M6 3l5 5-5 5" stroke="#fff" stroke-width="2.5" fill="none"/></svg></i></div></div>
  <div class="list-item"><div class="list-thumb" role="img" aria-label="Portrait of a news presenter" style="background:linear-gradient(135deg,#5a3a2a,#b48a70)"></div><div><p class="list-text">Lorem Ipsum is simply dummy text of the printing and typesetting industry. Lorem Ipsum standard dummy text.....</p><div class="list-actions"><span><svg><use href="#i-share"/></svg>Share Story <svg style="width:7px"><use href="#i-caret"/></svg></span><span><svg><use href="#i-save"/></svg>Save</span><span><svg><use href="#i-heart"/></svg>Vote</span></div></div></div>
  <div class="list-item"><div class="list-thumb" role="img" aria-label="Portrait of a woman in a blue top" style="background:linear-gradient(135deg,#2a3a6a,#a87a60)"></div><div><p class="list-text">Lorem Ipsum is simply dummy text of the printing and typesetting industry. Lorem Ipsum standard dummy text.....</p><div class="list-actions"><span><svg><use href="#i-share"/></svg>Share Story <svg style="width:7px"><use href="#i-caret"/></svg></span><span><svg><use href="#i-save"/></svg>Save</span><span><svg><use href="#i-heart"/></svg>Vote</span></div></div></div>
  <div class="list-item"><div class="list-thumb" role="img" aria-label="Man speaking in front of a red backdrop" style="background:linear-gradient(135deg,#9a2a2a,#6a5a5a)"></div><div><p class="list-text">Lorem Ipsum is simply dummy text of the printing and typesetting industry. Lorem Ipsum standard dummy text.....</p><div class="list-actions"><span><svg><use href="#i-share"/></svg>Share Story <svg style="width:7px"><use href="#i-caret"/></svg></span><span><svg><use href="#i-save"/></svg>Save</span><span><svg><use href="#i-heart"/></svg>Vote</span></div></div></div>
  <div class="list-item"><div class="list-thumb" role="img" aria-label="Portrait of an older man" style="background:linear-gradient(135deg,#3a3a3a,#8a7a70)"></div><div><p class="list-text">Lorem Ipsum is simply dummy text of the printing and typesetting industry. Lorem Ipsum standard dummy text.....</p><div class="list-actions"><span><svg><use href="#i-share"/></svg>Share Story <svg style="width:7px"><use href="#i-caret"/></svg></span><span><svg><use href="#i-save"/></svg>Save</span><span><svg><use href="#i-heart"/></svg>Vote</span></div></div></div>
</section>

<section class="story-list recent">
  <div class="list-head"><h2>RECENT STORIES</h2><div class="rail"></div><div class="nav"><i class="off"><svg class="icon" viewBox="0 0 16 16" style="width:10px"><path d="M10 3L5 8l5 5" stroke="#fff" stroke-width="2.5" fill="none"/></svg></i><i class="on"><svg class="icon" viewBox="0 0 16 16" style="width:10px"><path d="M6 3l5 5-5 5" stroke="#fff" stroke-width="2.5" fill="none"/></svg></i></div></div>
  <div class="list-item"><div class="list-thumb" role="img" aria-label="Portrait of a woman with dark hair" style="background:linear-gradient(135deg,#c8ccd2,#5a3a30)"></div><div><p class="list-text">Lorem Ipsum is simply dummy text of the printing and typesetting industry. Lorem Ipsum standard dummy text.....</p><div class="list-actions"><span><svg><use href="#i-share"/></svg>Share Story <svg style="width:7px"><use href="#i-caret"/></svg></span><span><svg><use href="#i-save"/></svg>Save</span><span><svg><use href="#i-heart"/></svg>Vote</span></div></div></div>
  <div class="list-item"><div class="list-thumb" role="img" aria-label="Man in a red shirt" style="background:linear-gradient(135deg,#d8d8d8,#c03030)"></div><div><p class="list-text">Lorem Ipsum is simply dummy text of the printing and typesetting industry. Lorem Ipsum standard dummy text.....</p><div class="list-actions"><span><svg><use href="#i-share"/></svg>Share Story <svg style="width:7px"><use href="#i-caret"/></svg></span><span><svg><use href="#i-save"/></svg>Save</span><span><svg><use href="#i-heart"/></svg>Vote</span></div></div></div>
  <div class="list-item"><div class="list-thumb" role="img" aria-label="Portrait of a blonde woman" style="background:linear-gradient(135deg,#e6d2a0,#b08a5a)"></div><div><p class="list-text">Lorem Ipsum is simply dummy text of the printing and typesetting industry. Lorem Ipsum standard dummy text.....</p><div class="list-actions"><span><svg><use href="#i-share"/></svg>Share Story <svg style="width:7px"><use href="#i-caret"/></svg></span><span><svg><use href="#i-save"/></svg>Save</span><span><svg><use href="#i-heart"/></svg>Vote</span></div></div></div>
  <div class="list-item"><div class="list-thumb" role="img" aria-label="Man in a suit at a podium" style="background:linear-gradient(135deg,#9ab0c8,#2a3040)"></div><div><p class="list-text">Lorem Ipsum is simply dummy text of the printing and typesetting industry. Lorem Ipsum standard dummy text.....</p><div class="list-actions"><span><svg><use href="#i-share"/></svg>Share Story <svg style="width:7px"><use href="#i-caret"/></svg></span><span><svg><use href="#i-save"/></svg>Save</span><span><svg><use href="#i-heart"/></svg>Vote</span></div></div></div>
</section>

<footer class="site-footer">
  <h3>Quick links</h3>
  <nav class="footer-links"><a class="current" href="#">Home</a><em>|</em><a href="#">About Us</a><em>|</em><a href="#">FAQ's</a><em>|</em><a href="#">Subscribe Now</a><em>|</em><a href="#">Contact Us</a></nav>
  <div class="footer-brand">Vorlet</div>
  <div class="follow">Follow us on</div>
  <div class="social-dots" aria-label="Social networks"><i></i><i></i><i></i><i></i><i></i><i></i><i></i><i></i></div>
</footer>
<div class="copyright">© 2014 Vorlet. All Rights Reserved. <a href="#">Terms</a> and <a href="#">Conditions</a></div>
</body>
</html>
```